Website for business consultancy - bright and happy feel needed

I need a website with 3/4 pages. I want the first page designed first and the rest will be easy. I need some pictures but none with corporate looking people. I need links to quillpost and deskroster. I need a contact form. I have samples of websites i like, fonts i like and I need a small logo also. I like simple, clean lines and I want a bright, happy and feminine feel. My audience are small businesses so I don't want them intimidated by new much of a corporate feel.
Updates

Target Market(s)

Small medium size businesses who want to grow and need that help but they cannot afford a full time financial director.

Industry/Entity Type

Business Consultant

Number of Pages Required

4 page

Other font styles liked:
• i can attach images

Colors
fcf0f6
e667a6
85cae6
ffffff
fbee3e

Requirements
Must have
• Link to quillpost and desk roster
• Contact form linked to my email
• Pictures - full width images where required
• Colour
• Mobile ready
• Soft feminine feel to it
• I dont want it to look like a corporate business consultancy - much more marketing or interior deign feel
Nice to have
• I would like the 3 services I have in 3 boxes that you click and takes you to a place with more information on the service.
• pictures thinking outside of the box
• Can be wordpress if need be
Should not have
• pictures with too much of a corporate feel
• No pictures of coporate people at all
• i like the following websites
• www.marbelquint.co.uk and others that are attached in the documents with a feminine feel to them

```html
<!DOCTYPE html>
<html lang="en">
<head>
<meta charset="utf-8">
<title>Maren Holt Consulting</title>
<link href="https://fonts.googleapis.com/css2?family=Lato:wght@300;400&display=swap" rel="stylesheet">
<style>
:root{
  --blush:#fcf0f6;
  --pink:#e667a6;
  --pink-deep:#c9558f;
  --sky:#85cae6;
  --sky-deep:#5aa9c9;
  --sun:#fbee3e;
  --white:#ffffff;
  --ink:#3a2a33;
  --muted:#9a8a93;
  --field-border:#d9a3bf;
}
*{box-sizing:border-box;margin:0;padding:0}
html,body{width:1200px;height:958px;overflow:hidden}
body{font-family:'Lato',sans-serif;font-weight:300;color:var(--ink);background:var(--blush);position:relative}
.site-header{height:98px;background:var(--blush);display:flex;justify-content:center;align-items:center}
.brand{display:flex;align-items:center;gap:12px;color:var(--pink);font-size:30px;font-weight:300;line-height:1;text-decoration:none}
.brand-dot{width:14px;height:14px;border-radius:50%;background:var(--pink)}
.main-nav{position:relative;height:29px;background:var(--pink)}
.main-nav a{color:var(--white);text-decoration:none;font-size:12px;line-height:29px;text-transform:uppercase;position:absolute;transform:translateX(-50%);font-weight:400}
.hero{position:absolute;top:127px;left:0;width:1200px;height:421px}
.hero-photo{position:absolute;inset:0;background:linear-gradient(100deg,var(--sky-deep) 0%,var(--sky) 40%,#d58bb6 70%,var(--pink-deep) 100%)}
.hero-shade{position:absolute;inset:0;background:rgba(110,40,85,.28)}
.hero-title{position:absolute;top:68px;width:100%;text-align:center;color:var(--white);font-size:26px;font-weight:300;letter-spacing:.3px}
.service{position:absolute;top:177px;width:262px;height:164px;border:1px solid var(--white);color:var(--white);text-align:center}
.service-icon{position:absolute;left:50%;top:-36px;transform:translateX(-50%);width:70px;height:70px;border:1px solid var(--white);background:var(--pink);display:flex;align-items:center;justify-content:center}
.service-title{margin-top:46px;font-size:19px;font-weight:300;text-transform:uppercase}
.service-rule{width:122px;height:1px;background:var(--white);margin:5px auto 12px}
.service-text{font-size:11.4px;line-height:18px;padding:0 24px}
.service-link{position:absolute;left:50%;bottom:-11px;transform:translateX(-50%);background:var(--sun);color:var(--ink);font-size:11px;line-height:22px;width:84px;text-transform:uppercase;text-decoration:none;font-weight:400}
.content{position:absolute;top:548px;left:0;width:1200px;height:372px;background:var(--blush)}
.col{position:absolute;top:24px}
.col-left{left:172px;width:416px}
.col-right{left:613px;width:417px}
.section-title{font-size:22px;font-weight:300;text-transform:uppercase;padding-bottom:3px;border-bottom:1px solid var(--sky);color:var(--pink-deep)}
.section-text{font-size:11px;line-height:18px;margin-top:14px}
.contact-form{margin-top:14px;display:grid;grid-template-columns:198px 198px;column-gap:19px;row-gap:18px}
.contact-form input,.contact-form textarea{font-family:inherit;font-weight:300;font-size:11px;border:1px solid var(--field-border);background:var(--white);padding:0 8px;height:28px;color:var(--ink)}
.contact-form ::placeholder{color:var(--muted)}
.contact-form textarea{grid-column:span 2;height:86px;padding-top:6px;resize:none}
.contact-form button{width:62px;height:26px;background:var(--pink);color:var(--white);border:none;font-family:inherit;font-size:11.4px;text-transform:uppercase}
.reach{margin-top:22px}
.reach-list{list-style:none;margin-top:13px}
.reach-list li{display:flex;gap:12px;font-size:11px;line-height:18px;margin-bottom:12px}
.reach-list svg{flex:none;margin-top:3px}
.social{display:flex;gap:18px;margin-top:4px}
.social span{width:12px;height:12px;border-radius:50%;background:var(--sky)}
.site-footer{position:absolute;top:920px;left:0;width:1200px;height:38px;background:var(--pink);color:var(--white);font-size:11.2px;display:flex;align-items:center;justify-content:space-between;padding:0 172px}
.site-footer a{color:var(--white);text-decoration:none}
.site-footer .sep{margin:0 6px}
</style>
</head>
<body>
<header class="site-header">
  <a class="brand" href="#"><span class="brand-dot"></span>Maren Holt Consulting</a>
</header>
<nav class="main-nav">
  <a href="#" style="left:304px">Home</a>
  <a href="#" style="left:396px">Profile</a>
  <a href="#" style="left:502px">Marketing</a>
  <a href="#" style="left:612px">Finance</a>
  <a href="#" style="left:748px">Business Marketing</a>
  <a href="#" style="left:886px">Contact</a>
</nav>

<section class="hero">
  <div class="hero-photo" role="img" aria-label="Photo of business colleagues shaking hands across a meeting table"></div>
  <div class="hero-shade"></div>
  <h1 class="hero-title">NOT ALL BUSINESS LOREM IPSUM IS SIMPLY DUMMY.</h1>

  <div class="service" style="left:172px">
    <div class="service-icon">
      <svg width="36" height="34" viewBox="0 0 36 34" fill="#fff"><g stroke="#fff" stroke-width="4"><path d="M13 1v24M1 13h24M4.5 4.5l17 17M21.5 4.5l-17 17"/></g><circle cx="13" cy="13" r="8"/><circle cx="13" cy="13" r="3" fill="#e667a6"/><g stroke="#fff" stroke-width="3"><path d="M27 17v16M19 25h16"/></g><circle cx="27" cy="25" r="5"/><circle cx="27" cy="25" r="2" fill="#e667a6"/></svg>
    </div>
    <h2 class="service-title">Business Coach Lorem</h2>
    <div class="service-rule"></div>
    <p class="service-text">Lorem Ipsum is simply dummy text of the printing and typesetting industry. Lorem Ipsum has been the industry's.</p>
    <a class="service-link" href="#">Know More</a>
  </div>

  <div class="service" style="left:468px">
    <div class="service-icon">
      <svg width="36" height="32" viewBox="0 0 36 32" fill="#fff"><rect x="3" y="22" width="5" height="8"/><rect x="11" y="17" width="5" height="13"/><rect x="19" y="19" width="5" height="11"/><rect x="27" y="12" width="5" height="18"/><path d="M2 17l9-8 6 5 11-10" stroke="#fff" stroke-width="2.5" fill="none"/><path d="M24 2h8v8z"/></svg>
    </div>
    <h2 class="service-title">Business Coach Lorem</h2>
    <div class="service-rule"></div>
    <p class="service-text">Lorem Ipsum is simply dummy text of the printing and typesetting industry. Lorem Ipsum has been the industry's.</p>
    <a class="service-link" href="#">Know More</a>
  </div>

  <div class="service" style="left:764px">
    <div class="service-icon">
      <svg width="26" height="30" viewBox="0 0 26 30" fill="#fff"><rect x="3" y="2" width="2.5" height="27"/><path d="M6 3c5-2 9 3 17 0v12c-8 3-12-2-17 0z"/></svg>
    </div>
    <h2 class="service-title">Business Coach Lorem</h2>
    <div class="service-rule"></div>
    <p class="service-text">Lorem Ipsum is simply dummy text of the printing and typesetting industry. Lorem Ipsum has been the industry's.</p>
    <a class="service-link" href="#">Know More</a>
  </div>
</section>

<main class="content">
  <div class="col col-left">
    <h2 class="section-title">Contact Form</h2>
    <p class="section-text">Lorem ipsum dolor sit amet, consectetur adipiscing elit. Sed interdum cursus hendrerit. Aliquam elementum velit dolor.</p>
    <form class="contact-form">
      <input type="text" placeholder="First Name">
      <input type="text" placeholder="Last Name">
      <input type="email" placeholder="Email Address">
      <input type="tel" placeholder="Phone Number">
      <textarea placeholder="Any Message"></textarea>
      <button type="submit">Submit</button>
    </form>
  </div>

  <div class="col col-right">
    <h2 class="section-title">About Us</h2>
    <p class="section-text">Lorem ipsum dolor sit amet, consectetur adipiscing elit. Sed interdum cursus hendrerit. Aliquam elementum velit dolor, non pellentesque turpis cursus non. Phasellus nec dignissim magna, non placerat tortor. Quisque tincidunt sem ac nulla commodo. Lorem ipsum dolor sit amet, consectetur adipiscing elit.</p>

    <div class="reach">
      <h2 class="section-title">Reach Us</h2>
      <ul class="reach-list">
        <li><svg width="9" height="12" viewBox="0 0 9 12"><path d="M4.5 0A4.5 4.5 0 0 0 0 4.5C0 8 4.5 12 4.5 12S9 8 9 4.5A4.5 4.5 0 0 0 4.5 0z" fill="#e667a6"/><circle cx="4.5" cy="4.5" r="1.6" fill="#fcf0f6"/></svg><span>04219, Carrer de les Oliveres 12, p.2, Vilanova del Riu, Girona<br>Vilanova del Riu - 41926 (United Kingdom)</span></li>
        <li><svg width="11" height="11" viewBox="0 0 11 11"><path d="M2.2 0l2 2.6-1.2 1.4c.7 1.6 2 2.9 3.6 3.6L8 6.4 11 8.6 9.8 10.6C4.8 10.6.4 6.2.4 1.2z" fill="#e667a6"/></svg><span>(+800) 555-014279</span></li>
        <li><svg width="11" height="9" viewBox="0 0 11 9"><rect width="11" height="9" fill="#e667a6"/><path d="M0 .5l5.5 4 5.5-4" stroke="#fcf0f6" fill="none"/></svg><span>info@marenholtconsulting.com</span></li>
      </ul>
      <div class="social" aria-label="Social links"><span></span><span></span><span></span><span></span><span></span></div>
    </div>
  </div>
</main>

<footer class="site-footer">
  <div><a href="#">Home</a><span class="sep">/</span><a href="#">About</a><span class="sep">/</span><a href="#">Business Marketing</a><span class="sep">/</span><a href="#">Privacy Terms</a><span class="sep">/</span><a href="#">Contacts</a></div>
  <div>© Copyright Maren Holt Consulting. All Rights Reserved.</div>
</footer>
</body>
</html>
```